LUMO - Óptica Clarena - web design and concept

Website concept - Create and develop our website design and structure. LUMO is an optical store chain, and we are looking to establish our web and digital concept. In attachment there are several pictures about our stores and our logo.

The website structure should be user friendly. Colors should be light and the design as simple and minimalist as possible. There are different variations of the logothat can be used, check the file.

The website will include optical collections and sun collections as an online store. Also, a medical menu should be considered in order for clients to schedule optometry appointments. There should also be a menu for client assistance where the clients can read about glass maintenance in our workshop.

Number of Pages Required

5+ page

Font styles to use
Serif
Sans Serif

Requirements
Must have
• Must be user-friendly and minimalist.
• Please USE PICTURES FROM THE BRANDS we sell: BRELO, MORVE, PKS, KOSU, NERAP
Nice to have
• Nice to inspire: ZEB glasses (see website https://ch.shopzeb-example.com/en/)
• Nice to inspire: https://brelo-eyewear-example.com/
• Nice to ispire: https://www.pksplanet-example.com/en/
Should not have
• Hysteric colors and shapes

```html
<!DOCTYPE html>
<html lang="en">
<head>
<meta charset="utf-8">
<title>LUMO – Óptica Clarena</title>
<link rel="stylesheet" href="https://fonts.googleapis.com/css2?family=Lato:wght@400;700&display=swap">
<style>
  :root {
    --bg: #ffffff;
    --ink: #111111;
    --text: #3a3a3a;
    --accent: #e8a23c;
    --button-bg: #000000;
    --button-text: #ffffff;
  }
  * { margin: 0; padding: 0; box-sizing: border-box; }
  html, body {
    width: 1200px;
    height: 139px;
    overflow: hidden;
    background: var(--bg);
    font-family: "Lato", Arial, sans-serif;
    color: var(--text);
  }
  .site-header {
    position: relative;
    width: 1200px;
    height: 139px;
  }
  .social-links {
    position: absolute;
    left: 161px;
    top: 16px;
    display: flex;
    gap: 11px;
    list-style: none;
  }
  .social-links li {
    width: 12px;
    height: 12px;
    border-radius: 50%;
    background: var(--ink);
  }
  .brand {
    position: absolute;
    left: 0;
    right: 0;
    top: 55px;
    text-align: center;
    color: var(--ink);
    line-height: 1;
  }
  .brand-name {
    display: block;
    font-size: 23px;
    font-weight: 400;
    letter-spacing: 5px;
    padding-left: 5px;
  }
  .brand-tagline {
    display: block;
    margin-top: 5px;
    font-size: 6px;
    letter-spacing: 1.6px;
    padding-left: 1.6px;
    text-transform: uppercase;
  }
  .header-tools {
    position: absolute;
    top: 15px;
    left: 819px;
    display: flex;
    align-items: center;
    font-size: 12.5px;
    color: var(--text);
  }
  .cart, .phone {
    display: flex;
    align-items: center;
  }
  .cart { gap: 7px; }
  .phone { gap: 5px; margin-left: 26px; }
  .cart-count { margin-left: -1px; }
  .main-nav {
    position: absolute;
    top: 102px;
    left: 0;
    right: 0;
    display: flex;
    justify-content: center;
    align-items: center;
    list-style: none;
    font-size: 12.5px;
  }
  .main-nav li { margin: 0 9.5px; }
  .main-nav a {
    color: var(--text);
    text-decoration: none;
  }
  .main-nav .is-current a { color: var(--accent); }
  .main-nav .appointment a {
    display: block;
    background: var(--button-bg);
    color: var(--button-text);
    padding: 4px 6px;
    line-height: 14px;
  }
</style>
</head>
<body>
<header class="site-header">
  <ul class="social-links" aria-label="Social networks">
    <li></li><li></li><li></li><li></li><li></li>
  </ul>

  <div class="brand">
    <span class="brand-name">LUMO</span>
    <span class="brand-tagline">Óptica Clarena</span>
  </div>

  <div class="header-tools">
    <div class="cart">
      <svg width="11" height="13" viewBox="0 0 11 13" aria-hidden="true">
        <path d="M3 4V3a2.5 2.5 0 0 1 5 0v1" fill="none" stroke="#111" stroke-width="1.3"/>
        <rect x="0.5" y="4" width="10" height="9" fill="#111"/>
      </svg>
      <span>Your Cart</span><span class="cart-count">( 0 )</span>
    </div>
    <div class="phone">
      <svg width="11" height="11" viewBox="0 0 24 24" aria-hidden="true">
        <path fill="#111" d="M6.6 10.8a15.1 15.1 0 0 0 6.6 6.6l2.2-2.2a1 1 0 0 1 1-.25 11.4 11.4 0 0 0 3.6.57 1 1 0 0 1 1 1V20a1 1 0 0 1-1 1A17 17 0 0 1 3 4a1 1 0 0 1 1-1h3.5a1 1 0 0 1 1 1c0 1.250.2 2.45.57 3.57a1 1 0 0 1-.25 1z"/>
      </svg>
      <span>+000-555-214-7</span>
    </div>
  </div>

  <nav>
    <ul class="main-nav">
      <li class="is-current"><a href="#">Home</a></li>
      <li><a href="#">Online store</a></li>
      <li><a href="#">Company history</a></li>
      <li><a href="#">Medical section</a></li>
      <li><a href="#">Store</a></li>
      <li><a href="#">Contact Us</a></li>
      <li class="appointment"><a href="#">Make an Appointment</a></li>
    </ul>
  </nav>
</header>
</body>
</html>
```